massage therapy Business Card Design

massage therapy business card
I would like a custom logo created as well.
My vision is angel wings with the HB business initials in between them.
A very simple design.
Colors preferred are light blues and greens.

Target Market(s)

Massage, Spa, fitness

Industry/Entity Type

Massage Therapy

Contact Information for Business Card

A Harbor Breeze
Nora Campe
Massage Therapist and Veldane Pulse Method Practitioner
2870 Marlow Ridge Road, Ashford, OR 97339
541-384-6190
nora.harborbreeze@mailvinto.com

Colors
abd036
33a6d7
3176b5
0255a3
0392cd
9bcb3c
cadf82

Requirements
Must have
• the logo must have angel wing.

```html
<!DOCTYPE html>
<html lang="en">
<head>
<meta charset="utf-8">
<title>A Harbor Breeze – Business Card</title>
<link href="https://fonts.googleapis.com/css2?family=Montserrat:wght@600;700;800&display=swap" rel="stylesheet">
<style>
  :root {
    --green: #8dc63f;
    --sky: #1c9ad6;
    --deep-blue: #0a6db8;
    --rule: #e3e3e3;
    --paper: #ffffff;
  }
  html, body {
    margin: 0;
    padding: 0;
    width: 1200px;
    height: 734px;
    overflow: hidden;
    background: var(--paper);
  }
  .card {
    position: relative;
    width: 1200px;
    height: 734px;
    background: var(--paper);
    font-family: "Montserrat", Arial, sans-serif;
  }
  .business-name {
    position: absolute;
    top: 116px;
    left: 0;
    width: 100%;
    margin: 0;
    text-align: center;
    font-size: 52px;
    font-weight: 800;
    letter-spacing: 0.5px;
    color: var(--green);
    text-transform: uppercase;
    line-height: 1;
  }
  .owner-row {
    position: absolute;
    top: 181px;
    left: 0;
    width: 100%;
    display: flex;
    justify-content: center;
    align-items: center;
    gap: 24px;
  }
  .owner-rule {
    width: 141px;
    height: 2px;
    background: var(--rule);
  }
  .owner-name {
    margin: 0;
    font-size: 29px;
    font-weight: 800;
    color: var(--sky);
    text-transform: uppercase;
    letter-spacing: 0.5px;
    line-height: 1;
  }
  .brand-mark {
    position: absolute;
    top: 312px;
    left: 0;
    width: 100%;
    display: flex;
    justify-content: center;
    align-items: center;
    gap: 22px;
  }
  .brand-dot {
    width: 70px;
    height: 70px;
    border-radius: 50%;
    background: var(--sky);
  }
  .brand-initials {
    font-size: 84px;
    font-weight: 800;
    color: var(--sky);
    line-height: 1;
  }
  .divider {
    position: absolute;
    top: 548px;
    left: 240px;
    width: 720px;
    height: 2px;
    background: var(--rule);
  }
  .contact {
    position: absolute;
    top: 561px;
    left: 0;
    width: 100%;
    margin: 0;
    text-align: center;
    font-style: normal;
    font-weight: 700;
    font-size: 23.5px;
    line-height: 35px;
    color: var(--deep-blue);
  }
  .contact .email {
    color: var(--green);
    font-weight: 600;
  }
</style>
</head>
<body>
  <main class="card">
    <h1 class="business-name">A Harbor Breeze</h1>
    <div class="owner-row">
      <span class="owner-rule"></span>
      <h2 class="owner-name">Nora Campe</h2>
      <span class="owner-rule"></span>
    </div>
    <div class="brand-mark">
      <span class="brand-dot"></span>
      <span class="brand-initials">HB</span>
    </div>
    <div class="divider"></div>
    <address class="contact">
      <div class="role">Massage Therapist and Veldane Pulse Method Practitioner</div>
      <div class="location">2870 Marlow Ridge Road, Ashford, OR 97339, 541-384-6190</div>
      <div class="email">nora.harborbreeze@mailvinto.com</div>
    </address>
  </main>
</body>
</html>
```